Plakat-Design für Oktoberfest-Veranstaltung
Zielgruppe
Ausrichten von Veranstaltungen. Das Firmenlogo ist dabei unrelevant.
Diese Veranstaltung wird neu aus dem Boden gestampft.
Zielgruppe für diese Art von Event sind sowohl junge Leute ab 18 Jahre, als auch ältere bis ca 60 Jahren.
Aufgabenstellung
Das fertige Plakat / Logo soll später auf Bauzaunplane gedruckt werden.
Bauzäune haben ein Maß von ca. 3,5 Meter Breite und 2 Meter Höhe.
Ein Beispiel für das Format hänge ich per Dateiupload an.
Der Schwerpunkt liegt auf dem Namen der Veranstaltung "Oktoberfest".
Dies soll deutlich erkennbar sein. Außerdem sollen die Informationen "DGH Tannwiesen" gut lesbar sein, aber nicht mehr als 20 bis 30% vom Platz einnehmen.
Das Datum "30. September 2017" soll gut erkennbar sein.
Die Datei ist so zu gestalten, dass das Datum von uns im nächsten Jahr veränderbar ist.
Ansonsten soll das Plakat im Gesamtbild einfach in Richtung Oktoberfest gehen.
Gerne darf eine hübsche Frau mit Bierkrug dabei sein. Auch/oder ein Brezel oder ähnliches.
Frei nach dem Motto: Sex sells! Die Leuten sollen einen Anreiz haben auch hinzuschauen.
Dieses Plakat gilt als einfacher Hinweis auf die Veranstaltung.
Weitere Detailinformationen zu dieser Veranstaltung werden über das Internet bekannt gegeben und nicht im Plakat auftauchen.
Das Plakat sollte modern sein. Verspielt nur zu 50 %
Da ich diese Plattform zum ersten mal nutze, bin ich noch etwas unsicher, welche Angaben hier sehr entscheidend sind.
Wenn ihr was wissen möchtet, fragt mich einfach.
Vielen dank schon mal!

```html
<!DOCTYPE html>
<html lang="de">
<head>
<meta charset="utf-8">
<title>Oktoberfest – DGH Tannwiesen</title>
<link rel="stylesheet" href="https://fonts.googleapis.com/css2?family=Roboto+Slab:wght@900&family=Open+Sans:wght@800&family=Bitter:wght@400&display=swap">
<style>
  :root {
    --bavaria-blue: #0b6db3;
    --check-light: #e6f1f9;
    --check-mid: #bcd9ee;
    --date-orange: #f5a300;
    --date-orange-deep: #e08600;
    --white: #ffffff;
    --photo-top: #b9c6d0;
    --photo-mid: #d9d4cb;
    --photo-bottom: #8a7a6a;
  }
  html, body {
    margin: 0;
    padding: 0;
    width: 1200px;
    height: 686px;
    overflow: hidden;
    background: var(--check-light);
  }
  .poster {
    position: relative;
    width: 1200px;
    height: 686px;
  }
  .poster svg { display: block; }
  .event-title {
    font-family: "Roboto Slab", "Rockwell", serif;
    font-weight: 900;
    font-size: 136px;
    fill: var(--white);
  }
  .event-date {
    font-family: "Open Sans", "Arial", sans-serif;
    font-weight: 800;
    font-size: 98px;
    fill: var(--white);
  }
  .event-venue {
    font-family: "Bitter", "Georgia", serif;
    font-weight: 400;
    font-size: 47px;
    letter-spacing: 1px;
    fill: var(--white);
  }
  .dots {
    fill: none;
    stroke-linecap: round;
    stroke-dasharray: 0 7.5;
  }
  .dots--blue { stroke: var(--bavaria-blue); stroke-width: 4; }
  .dots--white { stroke: var(--white); stroke-width: 3.5; }
</style>
</head>
<body>
<main class="poster">
  <svg width="1200" height="686" viewBox="0 0 1200 686" xmlns="http://www.w3.org/2000/svg">
    <defs>
      <linearGradient id="checkTone" x1="0" y1="0" x2="1" y2="1">
        <stop offset="0" stop-color="var(--check-light)"/>
        <stop offset="1" stop-color="var(--check-mid)"/>
      </linearGradient>
      <radialGradient id="dateTone" cx="0.45" cy="0.4" r="0.65">
        <stop offset="0" stop-color="var(--date-orange)"/>
        <stop offset="1" stop-color="var(--date-orange-deep)"/>
      </radialGradient>
      <linearGradient id="photoTone" x1="0" y1="0" x2="0" y2="1">
        <stop offset="0" stop-color="var(--photo-top)" stop-opacity="0.35"/>
        <stop offset="0.5" stop-color="var(--photo-mid)" stop-opacity="0.7"/>
        <stop offset="1" stop-color="var(--photo-bottom)" stop-opacity="0.8"/>
      </linearGradient>
    </defs>

    <rect class="backdrop" width="1200" height="686" fill="url(#checkTone)" role="img" aria-label="Hellblau-weißes Karomuster im bayerischen Stil"/>

    <rect class="mascot-photo" x="560" y="205" width="560" height="481" rx="24" fill="url(#photoTone)" role="img" aria-label="Foto: Mops in bayerischer Tracht mit Trachtenhut, Lederhose, Lebkuchenherz und Maßkrug Bier"/>

    <g class="title-ribbon">
      <path class="dots dots--blue" d="M23 58 L1167 17"/>
      <path d="M23 70 L1170 29 L1109 96 L1176 157 L29 197 L78 136 Z" fill="var(--bavaria-blue)"/>
      <path class="dots dots--blue" d="M26 212 L1176 171"/>
      <text class="event-title" x="108" y="172" textLength="958" lengthAdjust="spacingAndGlyphs" transform="rotate(-2 108 172)">OKTOBERFEST</text>
    </g>

    <g class="date-badge">
      <circle cx="273" cy="415" r="154" fill="url(#dateTone)"/>
      <g transform="rotate(-5 273 415)">
        <path class="dots dots--white" d="M170 336 L365 336"/>
        <text class="event-date" x="273" y="414" text-anchor="middle" textLength="236" lengthAdjust="spacingAndGlyphs">30.09</text>
        <text class="event-date" x="273" y="494" text-anchor="middle" textLength="200" lengthAdjust="spacingAndGlyphs">2017</text>
        <path class="dots dots--white" d="M180 514 L375 514"/>
      </g>
    </g>

    <g class="venue-band">
      <path class="dots dots--blue" d="M0 607 L1200 607"/>
      <rect x="0" y="617" width="1200" height="69" fill="var(--bavaria-blue)"/>
      <text class="event-venue" x="44" y="667">DGH Tannwiesen</text>
    </g>
  </svg>
</main>
</body>
</html>
```